Medical Implant company needs a Top Quality Premium Brochure

We need to create a top quality brochure for VIP clients, formed by top spine surgeons. The main goal here is to cause a deep quality impact, positioning the company and it´s solutions above the others, with a refined, unique and creative material.

Special paper, hot stamping, innovative format are welcome.

For more information check out our website: www.veltrosan.com.br (web translator are recommended for content understanding)

Veltrosan works with top quality spine and pain management products, providing solutions for the medical specialists, investing in high quality processes and continued medical education.

Short briefing:
1 - Company profile
2 - Quality / vision
3 - Continued education programs
4 - Main products
5 - Main partners
6 - Final stuff (creative final thoughts / considerations)

FORMAT: 25 x 18,5 cm (horizontal)
PAGES - 16

REFERENCES:

https://www.folivenk.net/gallery/52917340/Medical-Healthcare-Profile-Brochure

https://www.folivenk.net/gallery/7810263/TK-Alpine-Style-Brochure

Target Market(s)

Mainly brazilian spine and neuro surgeons with minimally invasive surgery skills.

Industry/Entity Type

Education

Requirements
Must have

• 18 pages design

1. Cover
2. IMAGE + TITLE - About Us
3. IMAGE + TEXT - About Us
4. IMAGE + TITLE - Vision
5. IMAGE + TEXT - Vision
6. IMAGE + TITLE - Quality
7. IMAGE + TEXT - Quality
8. Timeline Left
9. Timeline Right
10. IMAGE + TITLE - Medical Education
11. IMAGE + TEXT - Medical Education
12. IMAGE + TITLE - Minimally Invasive Technology
13. IMAGE + TEXT - Minimally Invasive Technology
14. IMAGE + TITLE - Impact Phrase
15. IMAGE + TEXT - Impact Phrase
16. Back

As longs as the text is under development and will be placed internally in the winning design, please use 'lorem ipsum' for text areas. The titles can follow the index above.

Nice to have
• The use of office pictures with some style / artistic finish in pages "about us"

```html
<!DOCTYPE html>
<html lang="pt-BR">
<head>
<meta charset="utf-8">
<title>Veltrosan – Brochure Spreads</title>
<link href="https://fonts.googleapis.com/css2?family=Open+Sans:wght@300;400;600;700&display=swap" rel="stylesheet">
<style>
  :root {
    --bg: #e4e4e4;
    --paper: #f7f7f7;
    --gold: #dca926;
    --charcoal: #4a4a4a;
    --title-grey: #9b9b9b;
    --text-grey: #8a8a8a;
    --green: #1e9a55;
    --green-dark: #178447;
    --green-light: #36b56c;
    --white: #ffffff;
  }
  * { box-sizing: border-box; margin: 0; padding: 0; }
  html, body { width: 1200px; height: 874px; overflow: hidden; }
  body {
    background: var(--bg);
    font-family: "Open Sans", Arial, sans-serif;
    position: relative;
  }
  .spread {
    position: absolute;
    left: 50px;
    width: 1100px;
    height: 407px;
    display: flex;
    box-shadow: 0 6px 18px rgba(0,0,0,.12);
  }
  .spread--quality { top: 20px; }
  .spread--products { top: 447px; }
  .page {
    position: relative;
    width: 550px;
    height: 407px;
    background: var(--paper);
    overflow: hidden;
  }
  .bar { position: absolute; height: 6px; }
  .bar--gold { background: var(--gold); }
  .bar--green { background: var(--green); }
  .bar--white { background: var(--white); }

  /* Spread 1 – left photo page */
  .photo-implant {
    position: absolute; inset: 0;
    background:
      radial-gradient(ellipse at 45% 40%, #6e6e6e 0 8%, transparent 22%),
      radial-gradient(ellipse at 55% 75%, #e3a35a 0 10%, transparent 30%),
      linear-gradient(160deg, #d9d7d2 0%, #ece9e3 40%, #cfc9c0 70%, #e8e4dc 100%);
  }
  .callout { position: absolute; left: 60px; top: 205px; width: 200px; height: 200px; }
  .callout svg { position: absolute; inset: 0; }
  .callout__text {
    position: absolute; top: 42px; width: 84px;
    font-size: 10.5px; line-height: 1.3; color: var(--white);
  }
  .callout__text strong { display: block; font-weight: 700; font-size: 11.5px; }
  .callout__text--gold { left: 14px; text-align: right; font-size: 9px; }
  .callout__text--dark { left: 106px; }

  /* Spread 1 – right title page */
  .quality-title {
    position: absolute; left: 90px; top: 100px;
    font-size: 25px; font-weight: 300; line-height: 1.2; color: var(--title-grey);
  }
  .quality-title em { font-style: normal; font-weight: 600; color: var(--gold); }
  .quality-body {
    position: absolute; left: 90px; top: 210px; width: 280px;
    font-size: 7px; line-height: 1.5; color: var(--text-grey);
  }
  .quality-body p + p { margin-top: 6px; color: var(--charcoal); font-weight: 600; }
  .brand {
    position: absolute;
    display: flex; align-items: center; gap: 5px;
    font-size: 13px; font-weight: 600; color: #6d6d6d; letter-spacing: .2px;
  }
  .brand__dot { width: 7px; height: 7px; background: #6d6d6d; border-radius: 50%; }
  .brand--quality { left: 420px; top: 185px; }

  /* Spread 2 – products page */
  .product { position: absolute; top: 28px; width: 150px; }
  .product--one { left: 28px; }
  .product--two { left: 205px; }
  .product--three { left: 380px; width: 145px; }
  .product .bar { position: static; width: 130px; margin-bottom: 22px; }
  .product__visual { width: 130px; height: 70px; margin-bottom: 22px; border-radius: 2px; }
  .product__visual--graft { background: linear-gradient(180deg, #eef3f4, #cfdcde); }
  .product__visual--kit { background: linear-gradient(90deg, #e9e3e3 0 45%, #f2f2f2 45% 50%, #b44553 50% 100%); }
  .product__visual--device { background: linear-gradient(180deg, #f4f4f4, #dedede); width: 70px; height: 40px; }
  .product h3 { font-size: 10.5px; font-weight: 700; color: var(--green); margin-bottom: 4px; }
  .product p { font-size: 7px; line-height: 1.45; color: var(--text-grey); margin-bottom: 5px; }
  .product p strong { color: var(--charcoal); }
  .product p.product__note { color: var(--green-light); }
  .brand--products { left: 30px; top: 368px; }

  /* Spread 2 – green page */
  .page--green { background: linear-gradient(160deg, var(--green-dark), var(--green) 50%, #22a35c); }
  .green-title {
    position: absolute; left: 60px; top: 62px;
    font-size: 22px; font-weight: 300; color: var(--white);
  }
  .green-title strong { font-weight: 600; }
  .green-copy {
    position: absolute; left: 60px; top: 100px; width: 440px;
    font-size: 7px; line-height: 1.5; color: rgba(255,255,255,.8);
  }
  .green-copy p { margin-bottom: 6px; }
  .green-copy .quote { border-left: 2px solid var(--white); padding-left: 8px; color: var(--white); }
  .green-copy .lead { color: var(--white); font-weight: 600; }
</style>
</head>
<body>

<section class="spread spread--quality">
  <div class="page page--photo">
    <div class="photo-implant" role="img" aria-label="Close-up photograph of a spinal screw implant fixed on a vertebra model"></div>
    <div class="bar bar--gold" style="left:0; top:40px; width:100px;"></div>
    <div class="callout">
      <svg viewBox="0 0 200 200" width="200" height="200" aria-hidden="true">
        <path d="M100 0 A100 100 0 0 0 100 200 Z" fill="var(--gold)"/>
        <path d="M100 0 A100 100 0 0 1 100 200 Z" fill="var(--charcoal)"/>
      </svg>
      <p class="callout__text callout__text--gold"><strong>Nunc eget</strong>euismod quam. Donec sit amet metus semper, porta vel nunc.</p>
      <p class="callout__text callout__text--dark"><strong>Aenean ut nisl</strong>vestibulum, rutrum tortor ut, cursus dolor.</p>
    </div>
  </div>
  <div class="page page--title">
    <div class="bar bar--gold" style="left:20px; top:48px; width:210px;"></div>
    <h2 class="quality-title">Scelerisque quis risus id<br><em>implantando qualidade</em><br>lacus duis eget diam</h2>
    <div class="quality-body">
      <p>Lorem ipsum dolor sit amet, consectetur adipiscing elit. Vestibulum tincidunt et imperdiet mollis, vitae porta nisl. Donec sed arcu et metus blandit.</p>
      <p>Aenean ut quis mi mattis. Pellentesque habitant morbi tristique senectus et netus.</p>
    </div>
    <div class="brand brand--quality"><span class="brand__dot"></span>Veltrosan</div>
    <div class="bar bar--gold" style="left:340px; top:330px; width:190px;"></div>
  </div>
</section>

<section class="spread spread--products">
  <div class="page page--products">
    <article class="product product--one">
      <div class="bar bar--green"></div>
      <div class="product__visual product__visual--graft" role="img" aria-label="Product photo of a bone graft package"></div>
      <h3>Phasellus placerat</h3>
      <p>Etiam et egestas tortor, nec elementum urna. Donec a consequat augue. <strong>Aenean eu ante eget nulla ultricies rhoncus quis quis ante.</strong> Morbi vulputate nunc a dictum volutpat.</p>
      <p class="product__note">Pellentesque consectetur tortor nisi sed pellentesque.</p>
      <p>Ut accumsan nulla ut dui sagittis, vel egestas lacus vestibulum. <strong>Suspendisse sagittis</strong> laoreet odio, at congue. Nunc pellentesque ut fringilla sagittis neque.</p>
    </article>
    <article class="product product--two">
      <div class="bar bar--green"></div>
      <div class="product__visual product__visual--kit" role="img" aria-label="Product photo of surgical kit boxes"></div>
      <h3>Aliquam a eleifend ipsum</h3>
      <p>Nunc felis metus, imperdiet a eros eget, condimentum ultrices massa. Pellentesque varius purus id dignissim. <strong>Etiam ipsum erat, cursus id nulla imperdiet, blandit egestas turpis.</strong> Pellentesque varius euismod orci eget maximus.</p>
      <p class="product__note">Duis vulputate posuere diam at cursus. Pellentesque eros erat, vestibulum sed nisi.</p>
    </article>
    <article class="product product--three">
      <div class="bar bar--green" style="width:120px;"></div>
      <div class="product__visual product__visual--device" role="img" aria-label="Product photo of a small medical device"></div>
      <h3 style="font-size:8px;">Phasellus id amet ornare</h3>
      <p><strong>Nulla suscipit eros nisi, at vehicula ultrices mi erat.</strong></p>
      <p class="product__note">Proin suscipit at tortor ut mattis feugiat dolor.</p>
      <p>Aliquam at lectus a lorem tincidunt euismod, vitae commodo nisl vel.</p>
    </article>
    <div class="brand brand--products"><span class="brand__dot"></span>Veltrosan</div>
  </div>
  <div class="page page--green">
    <h2 class="green-title">Scelerisque <strong>quis risus</strong> id implantando</h2>
    <div class="green-copy">
      <p>Lorem ipsum dolor sit amet, consectetur adipiscing elit. Vestibulum in metus ut est imperdiet mollis vitae felis. Sed congue rutrum metus.</p>
      <p class="quote">Nunc eget euismod quam. Donec sit amet metus semper porta vel nunc. Aenean ut nisl vestibulum, rutrum tortor ut, cursus dolor. Nulla facilisi.</p>
      <p>Duis vitae sapien quis ex luctus tempus. Mauris sed lectus ut orci aliquam tempor. Integer magna felis.</p>
      <p class="lead">Aenean ut quis mi mattis. Pellentesque habitant morbi tristique senectus et netus et malesuada fames ac turpis egestas.</p>
    </div>
    <div class="bar bar--white" style="left:330px; top:360px; width:210px;"></div>
  </div>
</section>

</body>
</html>
```